PLANKHUB.NET Single Product Based Website

We are one of the largest Stockiest of Diesel Engine (Marine and Power Plants) Spare Parts, this site will be focusing on a Single Product / Spare Parts - Connecting Rods <br/>We attached some actual pictures of the product and the Logo,<br/><br/>Once we approved your design shall provide with some contends and 10 actual Pictures to be added , should be a single page website SEO friendly sources to be used<br/>Should be Desktop, laptop and mobile friendly <br/><br/>best regards<br/>Oliver <br/>

Coding

Coded - Design and coding required

Number of Pages Required

1 page

Font styles to use
Other font styles liked:
• Book Antigua, Book Man Old Style or the designer can suggest

Colors

Designer to choose colors to be used in the design.

Requirements
Must have
• The Logo and same theme / colors can be used
Nice to have
• We shall provide the actual pictures of the product from our gallery approx 10 pictures to be added at final stage
Should not have
• other than initial design purpose , do not use any pictures downloaded from the internet

```html
<!DOCTYPE html>
<html lang="en">
<head>
<meta charset="utf-8">
<title>PLANKHUB.NET – Connecting Rods</title>
<link rel="stylesheet" href="https://fonts.googleapis.com/css2?family=Libre+Baskerville:wght@400;700&family=Crimson+Text:wght@400;600&display=swap">
<style>
:root{
  --orange:#f0502a;
  --orange-dark:#d9431f;
  --navy:#203f87;
  --ink:#2b2b2b;
  --muted:#777;
  --light:#f2f2f2;
  --white:#fff;
  --star:#f5a623;
  --serif-head:"Libre Baskerville",serif;
  --serif-body:"Crimson Text",serif;
}
*{box-sizing:border-box;margin:0;padding:0}
html,body{width:1200px;height:3908px;overflow:hidden}
body{position:relative;background:var(--white);font-family:var(--serif-body);color:var(--ink)}
.abs{position:absolute}
.btn{display:inline-block;background:var(--orange);color:var(--white);font-family:var(--serif-body);font-size:15px;letter-spacing:1px;border-radius:24px;text-align:center}
.photo{position:absolute}

/* header */
.topline{left:0;top:0;width:1200px;height:6px;background:var(--orange)}
.header{left:0;top:6px;width:1200px;height:106px;background:var(--white)}
.brand{position:absolute;display:flex;align-items:center;gap:10px;font-family:var(--serif-head);font-weight:700;color:var(--navy)}
.brand .dot{width:16px;height:16px;border-radius:50%;background:var(--orange)}
.header .brand{left:112px;top:36px;font-size:30px}
.nav{position:absolute;right:110px;top:44px;display:flex;gap:34px;font-size:15px;letter-spacing:1px}
.nav a{color:var(--ink);text-decoration:none}
.nav a.active{color:var(--orange)}

/* hero */
.hero{left:0;top:112px;width:1200px;height:720px;background:linear-gradient(120deg,#2b2f36 0%,#545a63 40%,#1c1f24 100%)}
.hero-title{left:790px;top:270px;font-family:var(--serif-head);font-size:40px;color:var(--white);letter-spacing:1px}
.hero-text{left:790px;top:340px;width:320px;font-size:14px;line-height:22px;color:#dcdcdc}
.hero .btn{}
.hero-btn{left:790px;top:450px;width:160px;height:46px;line-height:46px}
.dots{left:572px;top:796px;display:flex;gap:10px}
.dots span{width:10px;height:10px;border-radius:50%;background:#bbb}
.dots span.on{background:var(--white)}

/* welcome */
.welcome-title{left:0;top:950px;width:1200px;text-align:center;font-family:var(--serif-head);font-size:40px;color:var(--navy);letter-spacing:1px}
.welcome-title em{font-style:normal;color:var(--orange)}
.welcome-text{left:300px;top:1028px;width:600px;text-align:center;font-size:15px;line-height:25px;color:var(--muted)}
.welcome-btn{left:462px;top:1154px;width:276px;height:48px;line-height:48px}

/* products */
.products{left:0;top:1260px;width:1200px;height:390px;background:var(--light)}
.card{position:absolute;top:1278px;width:230px;height:355px;background:var(--white);text-align:center}
.card .photo{left:12px;top:12px;width:206px;height:200px}
.card .stars{position:absolute;left:0;top:228px;width:100%;color:var(--star);font-size:16px;letter-spacing:2px}
.card h3{position:absolute;left:0;top:258px;width:100%;font-family:var(--serif-head);font-weight:400;font-size:15px;letter-spacing:1px}
.card p{position:absolute;left:30px;top:288px;width:170px;font-size:13px;line-height:20px;color:var(--muted)}

/* feature */
.feature{left:0;top:1700px;width:620px;height:492px;background:var(--orange)}
.feature h2{position:absolute;left:112px;top:90px;width:460px;font-family:var(--serif-head);font-weight:400;font-size:24px;line-height:38px;color:var(--white);letter-spacing:1px}
.feature p{position:absolute;left:112px;top:196px;width:460px;font-size:15px;line-height:24px;color:#ffe2d8}
.feature .btn-dark{position:absolute;left:112px;top:360px;width:200px;height:52px;line-height:52px;border-radius:26px;background:#333;color:var(--white);text-align:center;font-size:16px;letter-spacing:1px}
.feature-photo{left:620px;top:1700px;width:580px;height:492px;background:linear-gradient(135deg,#c9c9c9,#8e8e8e 55%,#5b5b5b)}

/* product detail */
.main-photo{left:120px;top:2260px;width:448px;height:428px;background:linear-gradient(135deg,#cfa936,#8a7a4c 55%,#6c7590)}
.thumb{top:2704px;width:140px;height:124px}
.detail-title{left:606px;top:2312px;font-family:var(--serif-head);font-size:40px;color:var(--ink)}
.rating{left:606px;top:2380px;display:flex;align-items:center;gap:16px;font-size:14px;color:var(--muted)}
.rating .stars{color:var(--star);font-size:16px;letter-spacing:2px}
.price{left:606px;top:2424px;font-family:var(--serif-head);font-size:30px;display:flex;gap:40px}
.price s{color:var(--muted)}
.price b{color:var(--orange);font-weight:400}
.rule{left:606px;width:470px;height:1px;background:#ddd}
.detail-text{left:606px;top:2502px;width:470px;font-size:14px;line-height:24px;color:var(--muted)}
.qty{left:606px;top:2632px;display:flex;align-items:center;gap:10px;font-family:var(--serif-head);font-size:18px}
.qty .box{display:flex;border:1px solid #ccc;height:32px;align-items:center;font-family:var(--serif-body);font-size:15px}
.qty .box span{padding:0 10px;border-right:1px solid #ccc;line-height:30px}
.qty .box span:last-child{border-right:0}
.cart-btn{left:606px;top:2720px;width:158px;height:48px;line-height:48px;background:var(--orange);color:var(--white);text-align:center;font-size:15px;letter-spacing:1px}

/* gallery */
.gallery{left:0;top:2880px;width:1200px;height:640px;background:var(--light)}
.gallery-title{left:0;top:2924px;width:1200px;text-align:center;font-family:var(--serif-head);font-size:40px;color:var(--ink)}
.gallery-title em{font-style:normal;color:var(--orange)}

/* footer */
.footer{left:0;top:3540px;width:1200px;height:368px;background:var(--navy);color:var(--white)}
.footer .brand{left:112px;top:140px;font-size:28px;color:var(--white)}
.fcol{position:absolute;top:46px}
.fcol h4{font-family:var(--serif-head);font-weight:400;font-size:24px;margin-bottom:22px}
.fcol ul{list-style:none;font-size:15px;line-height:30px}
.fcol li::before{content:"";display:inline-block;width:6px;height:6px;border-radius:50%;background:var(--white);margin-right:16px;vertical-align:middle}
.fcol p{font-size:14px;line-height:22px;width:230px;color:#dfe5f3}
.email{margin-top:16px;width:230px;height:38px;background:var(--white);color:#888;font-size:13px;line-height:38px;padding-left:12px}
.submit{margin-top:10px;width:96px;height:32px;line-height:32px;background:var(--orange);color:var(--white);font-size:14px;text-align:center}
.copy{left:0;top:3860px;width:1200px;text-align:center;font-size:14px;color:#dfe5f3}
</style>
</head>
<body>

<div class="abs topline"></div>
<header class="abs header">
  <div class="brand"><span>PLANKHUB.NET</span><span class="dot"></span></div>
  <nav class="nav">
    <a class="active" href="#">HOME</a><a href="#">ABOUT US</a><a href="#">PRODUCTS</a><a href="#">GALLERY</a><a href="#">CONTACT US</a>
  </nav>
</header>

<section class="abs hero" role="img" aria-label="Engine parts: brake disc, pistons, gears and connecting rods on a dark background"></section>
<svg class="abs" style="left:0;top:712px" width="1200" height="120" viewBox="0 0 1200 120" aria-hidden="true">
  <path d="M0 40 Q600 170 1200 40 L1200 120 L0 120 Z" fill="#fff"/>
</svg>
<h1 class="abs hero-title">PLANKHUB.NET</h1>
<p class="abs hero-text">Built to exacting tolerances for marine engines and power plants, each rod is inspected, measured and certified before it leaves our stores.</p>
<a class="abs btn hero-btn">View More</a>
<div class="abs dots"><span class="on"></span><span></span><span></span></div>

<h2 class="abs welcome-title">WELCOME TO <em>PLANKHUB</em></h2>
<p class="abs welcome-text">We stock genuine connecting rods for diesel engines used in ships, generators and power plants. Every part is sourced from trusted makers, checked against factory specifications and kept ready for fast dispatch worldwide so your engine returns to service without long waiting times.</p>
<a class="abs btn welcome-btn">CLICK HERE FOR MORE INFO</a>

<section class="abs products"></section>
<div class="card" style="left:120px">
  <div class="photo" role="img" aria-label="Connecting rods on a workbench" style="background:linear-gradient(135deg,#9a8f7e,#5f5a52)"></div>
  <div class="stars">★★★★★</div><h3>PRODUCT NAME</h3><p>Forged steel rod for marine diesel engines</p>
</div>
<div class="card" style="left:366px">
  <div class="photo" role="img" aria-label="Row of connecting rods on a yellow tray" style="background:linear-gradient(135deg,#d9b63d,#7b7c88)"></div>
  <div class="stars">★★★★★</div><h3>PRODUCT NAME</h3><p>Forged steel rod for marine diesel engines</p>
</div>
<div class="card" style="left:612px">
  <div class="photo" role="img" aria-label="Connecting rods laid on a yellow surface" style="background:linear-gradient(135deg,#d4a92e,#6e6a66)"></div>
  <div class="stars">★★★★★</div><h3>PRODUCT NAME</h3><p>Forged steel rod for marine diesel engines</p>
</div>
<div class="card" style="left:858px">
  <div class="photo" role="img" aria-label="Single connecting rod close-up on grey floor" style="background:linear-gradient(135deg,#b6b6b6,#6c6c6c)"></div>
  <div class="stars">★★★★★</div><h3>PRODUCT NAME</h3><p>Forged steel rod for marine diesel engines</p>
</div>

<section class="abs feature">
  <h2>SED UT PERSPICIATIS UNDE<br>ISTE NATUS ERROR SIT VOLUPTATEM</h2>
  <p>Our stock covers rods, bearings, bolts and caps for the most common marine and stationary engines. Parts are stored in dry, controlled conditions and shipped with full inspection records, so fitters on site know exactly what they are installing.</p>
  <a class="btn-dark">VIEW DETAILS</a>
</section>
<div class="photo feature-photo" role="img" aria-label="Large polished connecting rod on a grey floor"></div>

<div class="photo main-photo" role="img" aria-label="Three connecting rods on a yellow background"></div>
<div class="photo thumb" style="left:120px;background:linear-gradient(135deg,#c9a63a,#6f7390)" role="img" aria-label="Thumbnail: rods on yellow tray"></div>
<div class="photo thumb" style="left:274px;background:linear-gradient(135deg,#a8a8a8,#5c5c5c)" role="img" aria-label="Thumbnail: single rod close-up"></div>
<div class="photo thumb" style="left:428px;background:linear-gradient(135deg,#8c8478,#4e4a45)" role="img" aria-label="Thumbnail: rods stacked in storage"></div>

<h2 class="abs detail-title">Diesel Engine</h2>
<div class="abs rating"><span class="stars">★★★★★</span><span>Genuine part in stock</span></div>
<div class="abs price"><s>£55.99</s><b>£25.99</b></div>
<div class="abs rule" style="top:2484px"></div>
<p class="abs detail-text">Complete connecting rod assembly with cap, bolts and bush, measured and tested for bore size, straightness and twist. Suitable for medium speed diesel engines in marine and power plant service.</p>
<div class="abs rule" style="top:2610px"></div>
<div class="abs qty">Qty : <div class="box"><span>+</span><span>01</span><span>−</span></div></div>
<a class="abs cart-btn">ADD TO CART</a>

<section class="abs gallery"></section>
<h2 class="abs gallery-title">Photo <em>Gallery</em></h2>
<div class="photo" style="left:120px;top:3028px;width:460px;height:212px;background:linear-gradient(135deg,#8a7e6c,#4f4840)" role="img" aria-label="Many connecting rods stored in racks"></div>
<div class="photo" style="left:592px;top:3028px;width:236px;height:212px;background:linear-gradient(135deg,#b0b0b0,#666)" role="img" aria-label="Connecting rod big end close-up"></div>
<div class="photo" style="left:840px;top:3028px;width:240px;height:212px;background:linear-gradient(135deg,#d6b13a,#767a8a)" role="img" aria-label="Rods laid on yellow tray"></div>
<div class="photo" style="left:120px;top:3252px;width:240px;height:220px;background:linear-gradient(135deg,#a39a8c,#5d5750)" role="img" aria-label="Connecting rod on workbench"></div>
<div class="photo" style="left:372px;top:3252px;width:328px;height:220px;background:linear-gradient(135deg,#bcbcbc,#777)" role="img" aria-label="Polished connecting rods side by side"></div>
<div class="photo" style="left:712px;top:3252px;width:368px;height:220px;background:linear-gradient(135deg,#b8b2a8,#6a6560)" role="img" aria-label="Connecting rod with cap on the floor"></div>

<footer class="abs footer">
  <div class="brand"><span>PLANKHUB.NET</span><span class="dot"></span></div>
  <div class="fcol" style="left:412px">
    <h4>Quick Links</h4>
    <ul><li>Home</li><li>About Us</li><li>Products</li><li>Gallery</li><li>Contact Us</li></ul>
  </div>
  <div class="fcol" style="left:620px">
    <h4>Courses</h4>
    <ul><li>Rod assemblies</li><li>Big end bearings</li><li>Piston pins</li><li>Bolts and nuts</li><li>Bushes</li></ul>
  </div>
  <div class="fcol" style="left:852px">
    <h4>Newsletter</h4>
    <p>Get stock updates and new arrivals in your inbox.</p>
    <div class="email">Enter Email id</div>
    <div class="submit">Submit</div>
  </div>
</footer>
<p class="abs copy">© Copyright 2020 Plankhub.net. All Rights Reserved</p>

</body>
</html>
```